Website - Enhance the look - finish my contact form - build about section

I already have most of the website coded, but I am sure it has minor errors and code improvements. Also, I want just to enhance the current look, take what I have and the images I have and make it look a little nicer if you can. The links, aside from the about and contact sections, can just be clicked but do not lead anywhere. I will build out the pages later. I can give you the login to the back end to upload the form PHP handling when it is ready, and have already set up public keys, etc. Note at www.fernquill.com/staging/ the logos have the correct wording below them, the uploaded logos have the wrong company names below them.

Target Market(s)

Clients saving money with $100,000 or more

Industry/Entity Type

Financial

Coding

Coded - Design and coding required

Number of Pages Required

1 page

Colors
0054AA
0677BA
7BADD7
CADEEF
E8F1F8
EB3D1F
EC4F4E
F09395
F8D3D4
FCEDEE

Requirements
Must have
• Contact form, follows my current content I have already typed in and flow, about me section where I can drop my picture and bio into the code later
Nice to have
• I have already provided an example of the site www.fernquill.com/staging/ I just want to make this look better but it has to follow the content I already have
Should not have
• For now do not have the links go anywhere aside from the contact, about, and home

```html
<!DOCTYPE html>
<html lang="en">
<head>
<meta charset="utf-8">
<title>Fernquill Wealth Planners</title>
<link href="https://fonts.googleapis.com/css2?family=Montserrat:wght@400;600;700;800;900&family=Open+Sans:wght@400;600;700&display=swap" rel="stylesheet">
<style>
:root{
  --red:#EB3D1F;
  --red-soft:#EC4F4E;
  --red-deep:#B8232B;
  --pink:#FCEDEE;
  --pink-mid:#F8D3D4;
  --ink:#1B1B1B;
  --dark:#151515;
  --grey:#5E5E5E;
  --line:#E3E3E3;
  --white:#FFFFFF;
}
*{margin:0;padding:0;box-sizing:border-box}
html,body{width:1200px;height:4228px;overflow:hidden}
body{font-family:"Open Sans",sans-serif;color:var(--ink);background:var(--white);font-size:13px}
h1,h2,h3,h4,.btn,.nav a,.brand{font-family:"Montserrat",sans-serif}
.btn{display:inline-block;background:var(--red);color:#fff;font-size:12px;font-weight:700;padding:11px 20px;border-radius:3px}
.btn-outline{background:transparent;border:1px solid #fff}
.section-title{font-size:30px;font-weight:800;text-align:center;text-transform:uppercase;letter-spacing:.5px}
.title-rule{width:60px;height:3px;background:var(--red);margin:10px auto 0}

/* hero */
.hero{position:relative;height:500px;background:linear-gradient(100deg,#222 0%,#2e2e2e 45%,#5b5b58 70%,#8a8883 100%);color:#fff}
.hero-photo{position:absolute;right:0;top:0;width:640px;height:500px;background:linear-gradient(120deg,#3a3a38,#76736d 55%,#a29e96)}
.site-header{position:absolute;top:0;left:0;right:0;height:70px;display:flex;align-items:center;padding:0 120px;z-index:2}
.brand{display:flex;align-items:center;gap:10px;font-weight:800;font-size:15px;letter-spacing:1px;text-transform:uppercase}
.brand-dot{width:22px;height:22px;background:var(--red);border-radius:50%}
.nav{margin-left:auto;display:flex;gap:22px;align-items:center}
.nav a{color:#fff;font-size:12px;font-weight:600;text-decoration:none}
.nav a.active{background:var(--red);padding:6px 10px;border-radius:2px}
.nav .btn{margin-left:30px;padding:9px 16px}
.hero-copy{position:absolute;left:120px;top:150px;z-index:2}
.hero-copy h1{font-size:46px;font-weight:800;line-height:1.1;text-transform:uppercase}
.hero-copy p{margin:14px 0 26px;font-size:14px;color:#ddd}
.hero-copy .btn+.btn{margin-left:10px}

/* badges */
.badges{height:90px;background:var(--dark);display:flex;align-items:center;justify-content:space-around;padding:0 120px}
.badge{width:130px;height:34px;background:#3a3a3a;border-radius:4px}

/* services */
.services{height:600px;padding-top:48px;background:#fff}
.services .lead{text-align:center;color:var(--grey);width:460px;margin:14px auto 0;font-size:13px}
.cards{display:flex;gap:24px;justify-content:center;margin-top:40px;position:relative}
.card{width:205px;height:215px;background:#fff;box-shadow:0 6px 24px rgba(0,0,0,.1);text-align:center;padding:26px 18px;border-radius:4px}
.card.featured{background:var(--red-deep);color:#fff;transform:translateY(-10px);height:235px}
.card-icon{width:44px;height:44px;margin:0 auto 16px;border:2px solid var(--red);border-radius:8px}
.card.featured .card-icon{border-color:#fff}
.card h3{font-size:13px;font-weight:800;text-transform:uppercase;margin-bottom:10px}
.card p{font-size:11px;line-height:1.5;color:var(--grey);margin-bottom:14px}
.card.featured p{color:#f3d8d8}
.card .btn{padding:7px 12px;font-size:10px}
.card.featured .btn{background:#fff;color:var(--red-deep)}
.arrow{position:absolute;top:95px;width:30px;height:30px}
.services .more{text-align:center;margin-top:50px}

/* about */
.about{height:400px;background:#F4F4F4;display:flex}
.about-photo{width:560px;height:400px;background:linear-gradient(135deg,#c7cdd3,#eef0f2 55%,#9aa4ae)}
.about-copy{padding:60px 120px 0 50px;flex:1}
.about-copy h2{font-size:30px;font-weight:800;text-transform:uppercase}
.about-copy p{font-size:12px;line-height:1.7;color:var(--grey);margin:14px 0}
.ticks{display:grid;grid-template-columns:1fr 1fr;gap:6px 20px;font-size:12px;margin-bottom:22px}
.ticks li{list-style:none;display:flex;gap:8px;align-items:center}

/* process */
.process{height:440px;padding-top:50px}
.steps{display:flex;justify-content:center;gap:34px;margin-top:60px;position:relative}
.step{width:140px;height:140px;border-radius:50%;background:var(--dark);color:#fff;display:flex;flex-direction:column;align-items:center;justify-content:center;text-align:center;padding:18px;border:4px solid #fff;box-shadow:0 0 0 3px var(--red)}
.step:nth-child(2),.step:nth-child(5){background:#2c2c2c}
.step b{font-family:Montserrat,sans-serif;font-size:22px;font-weight:800}
.step span{font-size:10px;line-height:1.35;margin-top:6px;font-weight:600}
.steps svg{position:absolute;top:-30px;left:0}

/* wordmark */
.wordmark{height:70px;text-align:center;font-family:Montserrat,sans-serif;font-size:62px;font-weight:900;color:transparent;-webkit-text-stroke:1px var(--pink-mid);letter-spacing:2px;line-height:70px;white-space:nowrap;overflow:hidden}

/* plan band */
.plan{height:340px;position:relative;background:linear-gradient(180deg,#2f4a33,#1d3424 50%,#2a3f2e);color:#fff}
.plan-copy{position:absolute;left:120px;top:120px}
.plan-copy h2{font-size:30px;font-weight:800;text-transform:uppercase}
.plan-copy p{font-size:12px;margin:6px 0 18px;color:#d6e1d6}

/* partners */
.partners{height:500px;display:flex;padding:50px 120px 0;gap:40px}
.partners-left{flex:1}
.partners-left h2{font-size:28px;font-weight:800;text-transform:uppercase;line-height:1.2}
.partners-left .rule{width:60px;height:3px;background:var(--red);margin:14px 0 24px}
.plist{display:grid;grid-template-columns:1fr 1fr;gap:0 30px}
.plist li{list-style:none;font-size:13px;padding:9px 0;border-bottom:1px solid var(--line);display:flex;gap:8px;align-items:center}
.plist li.on{background:var(--red);color:#fff;padding-left:10px;font-weight:700}
.plist li i{width:6px;height:6px;background:var(--red);border-radius:50%}
.plist li.on i{background:#fff}
.partner-card{width:500px;height:330px;background:var(--dark);color:#fff;display:flex;box-shadow:14px 14px 0 var(--pink-mid);margin-top:10px}
.partner-photo{width:250px;height:330px;background:radial-gradient(circle at 50% 55%,#c07a4a,#7a4428 50%,#2a2622)}
.partner-text{padding:80px 26px 0}
.partner-text h3{font-size:15px;font-weight:800;text-transform:uppercase}
.partner-text p{font-size:11px;line-height:1.6;color:#ccc;margin:10px 0 18px}

/* accounts */
.accounts{height:480px;background:var(--pink);padding-top:50px}
.acc-grid{display:grid;grid-template-columns:repeat(6,148px);gap:16px;justify-content:center;margin-top:44px}
.acc{height:110px;background:#fff;border-top:3px solid var(--red);padding:16px 12px;border-radius:2px;box-shadow:0 3px 10px rgba(0,0,0,.05)}
.acc svg{display:block;margin-bottom:10px}
.acc span{font-size:11px;font-weight:700;font-family:Montserrat,sans-serif;line-height:1.3}

/* testimonials */
.testimonials{height:340px;padding-top:44px}
.tgrid{display:flex;gap:24px;justify-content:center;margin-top:36px}
.tcard{width:300px;height:160px;background:#fff;border:1px solid var(--line);padding:20px;border-radius:3px;position:relative}
.tcard .q{font-family:Montserrat,sans-serif;font-size:34px;color:var(--red);line-height:20px}
.tcard p{font-size:10.5px;line-height:1.6;color:var(--grey);margin-top:6px}
.tcard .who{margin-top:12px;font-size:11px;font-weight:700;font-family:Montserrat,sans-serif;display:flex;align-items:center;gap:8px}
.tcard .who i{width:26px;height:26px;border-radius:50%;background:var(--pink-mid)}

/* cta */
.cta{height:220px;background:linear-gradient(180deg,var(--red-soft),var(--red-deep));color:#fff;text-align:center;padding-top:62px}
.cta h2{font-size:32px;font-weight:800;text-transform:uppercase}
.cta p{font-size:13px;margin:6px 0 20px;color:#fde}
.cta .btn{background:#fff;color:var(--red-deep)}

/* footer */
.footer{height:248px;background:var(--dark);color:#ccc;padding:36px 120px 0;position:relative}
.fcols{display:flex;gap:40px}
.fcol{flex:1;font-size:11px}
.fcol.first{flex:1.3}
.fcol h4{color:#fff;font-size:12px;font-weight:700;margin-bottom:14px;text-transform:uppercase}
.fcol li{list-style:none;margin-bottom:8px;display:flex;gap:6px;align-items:center}
.fcol li i{width:14px;height:14px;border-radius:50%;background:var(--red)}
.fcol p{line-height:1.6}
.sub-input{height:32px;background:#2a2a2a;border-radius:3px;margin:10px 0;padding:8px 10px;color:#888}
.copy{position:absolute;bottom:0;left:0;right:0;height:34px;border-top:1px solid #2c2c2c;text-align:center;line-height:34px;font-size:10px;color:#888}
</style>
</head>
<body>

<section class="hero">
  <div class="hero-photo" role="img" aria-label="Modern lounge chair and side table in a softly lit interior"></div>
  <header class="site-header">
    <div class="brand"><span class="brand-dot"></span>Fernquill</div>
    <nav class="nav">
      <a class="active">Home</a><a>About</a><a>Services</a><a>Contact</a>
      <span class="btn">Get Started</span>
    </nav>
  </header>
  <div class="hero-copy">
    <h1>Discover the rhythm<br>of innovation</h1>
    <p>Built supporting the place your money lives.</p>
    <span class="btn">Explore Our Brands</span><span class="btn btn-outline">Get In Touch</span>
  </div>
</section>

<section class="badges">
  <div class="badge"></div><div class="badge"></div><div class="badge"></div><div class="badge"></div>
</section>

<section class="services">
  <h2 class="section-title">Our Services</h2>
  <div class="title-rule"></div>
  <p class="lead">With over 20 years of experience in wealth planning, we support our advisors with solutions for every financial need.</p>
  <div class="cards">
    <svg class="arrow" style="left:110px" viewBox="0 0 30 30"><path d="M18 8l-7 7 7 7" stroke="#999" stroke-width="2" fill="none"/></svg>
    <div class="card"><div class="card-icon"></div><h3>Risk Management</h3><p>Insurance to protect income and assets, with clear advice for every family stage.</p><span class="btn">Learn More</span></div>
    <div class="card"><div class="card-icon"></div><h3>Tax Planning</h3><p>Comprehensive knowledge of the tax act and its use to keep more of your wealth.</p><span class="btn">Learn More</span></div>
    <div class="card featured"><div class="card-icon"></div><h3>Investment Management</h3><p>Experienced Chartered Investment Managers (CIM) with a disciplined long-term approach.</p><span class="btn">Learn More</span></div>
    <div class="card"><div class="card-icon"></div><h3>Estate Planning</h3><p>Ensure assets, wishes and legacy pass to the people you care about most.</p><span class="btn">Learn More</span></div>
    <svg class="arrow" style="right:110px" viewBox="0 0 30 30"><path d="M12 8l7 7-7 7" stroke="#999" stroke-width="2" fill="none"/></svg>
  </div>
  <div class="more"><span class="btn">Explore Our Services</span></div>
</section>

<section class="about">
  <div class="about-photo" role="img" aria-label="Advisors working together at computers in a bright office"></div>
  <div class="about-copy">
    <h2>About Fernquill</h2>
    <p>A collective of wealth, strategy and growth. Fernquill is a modern financial firm built to support families and business owners. We partner with seasoned professionals to provide the resources, infrastructure and guidance needed to thrive, so every client can build lasting wealth through considered planning, sound investing and steady review of the goals that matter.</p>
    <ul class="ticks">
      <li><svg width="14" height="14" viewBox="0 0 14 14"><path d="M2 7l3 3 7-7" stroke="#EB3D1F" stroke-width="2" fill="none"/></svg>Decades of experience</li>
      <li><svg width="14" height="14" viewBox="0 0 14 14"><path d="M2 7l3 3 7-7" stroke="#EB3D1F" stroke-width="2" fill="none"/></svg>Technically certified team</li>
      <li><svg width="14" height="14" viewBox="0 0 14 14"><path d="M2 7l3 3 7-7" stroke="#EB3D1F" stroke-width="2" fill="none"/></svg>Family-owned &amp; trusted</li>
      <li><svg width="14" height="14" viewBox="0 0 14 14"><path d="M2 7l3 3 7-7" stroke="#EB3D1F" stroke-width="2" fill="none"/></svg>Serving our local community</li>
    </ul>
    <span class="btn">Learn More About Us</span>
  </div>
</section>

<section class="process">
  <h2 class="section-title">Our Planning Process</h2>
  <div class="title-rule"></div>
  <div class="steps">
    <svg width="1200" height="220" viewBox="0 0 1200 220" fill="none" stroke="#EB3D1F" stroke-width="2">
      <path d="M220 40 Q275 0 330 40"/><path d="M394 180 Q449 220 504 180"/><path d="M568 40 Q623 0 678 40"/><path d="M742 180 Q797 220 852 180"/><path d="M916 40 Q971 0 1026 40"/>
    </svg>
    <div class="step"><b>01</b><span>Establish &amp; Define the Client-Planner Relationship</span></div>
    <div class="step"><b>02</b><span>Gather Client Data and Determine Goals</span></div>
    <div class="step"><b>03</b><span>Analyze and Evaluate the Client's Financial Status</span></div>
    <div class="step"><b>04</b><span>Develop and Present Financial Planning Recommendations</span></div>
    <div class="step"><b>05</b><span>Implement the Financial Planning Recommendations</span></div>
    <div class="step"><b>06</b><span>Monitor the Plan and the Financial Planning Relationship</span></div>
  </div>
</section>

<div class="wordmark">FERNQUILL WEALTH PLANNERS</div>

<section class="plan" role="img" aria-label="Aerial view of a green forest canopy">
  <div class="plan-copy">
    <h2>Everything in one financial plan</h2>
    <p>Coordinating all of your planning needs</p>
    <span class="btn btn-outline">Let's Connect</span>
  </div>
</section>

<section class="partners">
  <div class="partners-left">
    <h2>Trusted partnerships<br>with vetted financial<br>experts</h2>
    <div class="rule"></div>
    <ul class="plist">
      <li class="on"><i></i>Accountants</li><li><i></i>Real Estate Agents</li>
      <li><i></i>Lawyers</li><li><i></i>Business Consultants</li>
      <li><i></i>Mortgage specialist</li><li><i></i>Trust Specialist</li>
      <li><i></i>Actuaries</li><li><i></i>Business Valuators</li>
      <li><i></i>Property Valuators</li><li><i></i>Cross Border Specialist</li>
      <li><i></i>Banking providers</li><li><i></i>Health Specialist</li>
    </ul>
  </div>
  <div class="partner-card">
    <div class="partner-photo" role="img" aria-label="Cupped hands holding coins"></div>
    <div class="partner-text">
      <h3>Accountants</h3>
      <p>We work with accountants that understand our strategies. Save time by having us send your documents each year for preparation.</p>
      <span class="btn">Learn More</span>
    </div>
  </div>
</section>

<section class="accounts">
  <h2 class="section-title">Access to all account types</h2>
  <div class="title-rule"></div>
  <div class="acc-grid">
    <div class="acc"><svg width="22" height="22" viewBox="0 0 22 22"><rect x="3" y="5" width="16" height="12" rx="2" stroke="#EB3D1F" stroke-width="2" fill="none"/></svg><span>Non Registered</span></div>
    <div class="acc"><svg width="22" height="22" viewBox="0 0 22 22"><rect x="3" y="5" width="16" height="12" rx="2" stroke="#EB3D1F" stroke-width="2" fill="none"/></svg><span>Margin</span></div>
    <div class="acc"><svg width="22" height="22" viewBox="0 0 22 22"><rect x="3" y="5" width="16" height="12" rx="2" stroke="#EB3D1F" stroke-width="2" fill="none"/></svg><span>Tax Free TFSA</span></div>
    <div class="acc"><svg width="22" height="22" viewBox="0 0 22 22"><path d="M3 11l8-7 8 7v8H3z" stroke="#EB3D1F" stroke-width="2" fill="none"/></svg><span>First Home Savings Account FHSA</span></div>
    <div class="acc"><svg width="22" height="22" viewBox="0 0 22 22"><rect x="3" y="5" width="16" height="12" rx="2" stroke="#EB3D1F" stroke-width="2" fill="none"/></svg><span>Registered Savings RRSP</span></div>
    <div class="acc"><svg width="22" height="22" viewBox="0 0 22 22"><rect x="3" y="5" width="16" height="12" rx="2" stroke="#EB3D1F" stroke-width="2" fill="none"/></svg><span>Registered Income RRIF</span></div>
    <div class="acc"><svg width="22" height="22" viewBox="0 0 22 22"><rect x="5" y="10" width="12" height="9" stroke="#EB3D1F" stroke-width="2" fill="none"/><path d="M7 10V7a4 4 0 018 0v3" stroke="#EB3D1F" stroke-width="2" fill="none"/></svg><span>Locked In Retirement LIRA</span></div>
    <div class="acc"><svg width="22" height="22" viewBox="0 0 22 22"><rect x="5" y="10" width="12" height="9" stroke="#EB3D1F" stroke-width="2" fill="none"/><path d="M7 10V7a4 4 0 018 0v3" stroke="#EB3D1F" stroke-width="2" fill="none"/></svg><span>Locked In Registered LRSP</span></div>
    <div class="acc"><svg width="22" height="22" viewBox="0 0 22 22"><rect x="5" y="10" width="12" height="9" stroke="#EB3D1F" stroke-width="2" fill="none"/><path d="M7 10V7a4 4 0 018 0v3" stroke="#EB3D1F" stroke-width="2" fill="none"/></svg><span>Locked-In Life Income LLIF</span></div>
    <div class="acc"><svg width="22" height="22" viewBox="0 0 22 22"><circle cx="11" cy="8" r="4" stroke="#EB3D1F" stroke-width="2" fill="none"/><path d="M4 19c1-4 13-4 14 0" stroke="#EB3D1F" stroke-width="2" fill="none"/></svg><span>Individual Pension IPP</span></div>
    <div class="acc"><svg width="22" height="22" viewBox="0 0 22 22"><rect x="3" y="5" width="16" height="12" rx="2" stroke="#EB3D1F" stroke-width="2" fill="none"/></svg><span>Trust Accounts</span></div>
    <div class="acc"><svg width="22" height="22" viewBox="0 0 22 22"><path d="M11 18l-7-7a4 4 0 017-4 4 4 0 017 4z" stroke="#EB3D1F" stroke-width="2" fill="none"/></svg><span>Donor Advised DAF</span></div>
  </div>
</section>

<section class="testimonials">
  <h2 class="section-title">Testimonials</h2>
  <div class="title-rule"></div>
  <div class="tgrid">
    <div class="tcard"><div class="q">“</div><p>Working with the team has been a smooth experience from day one. They explained every option clearly and helped us set goals we understand and feel confident about for the future.</p><div class="who"><i></i>DANA K.</div></div>
    <div class="tcard"><div class="q">“</div><p>I wanted a planner who would take the time to listen. Every meeting is organized, every question answered, and I finally have one plan that brings all my accounts together.</p><div class="who"><i></i>TOM L.</div></div>
    <div class="tcard"><div class="q">“</div><p>We have trusted them through retirement and a family move. Their advice is practical, honest and patient, and we always leave knowing exactly what comes next.</p><div class="who"><i></i>DANA K.</div></div>
  </div>
</section>

<section class="cta">
  <h2>Let's bring your vision to life</h2>
  <p>Experience the difference of working with a team that values integrity, transparency and results.</p>
  <span class="btn">Get Started Today</span>
</section>

<footer class="footer">
  <div class="fcols">
    <div class="fcol first">
      <div class="brand" style="color:#fff;margin-bottom:14px"><span class="brand-dot"></span>Fernquill</div>
      <p>Proud members of an independent dealer network. Fernquill Wealth Planners is a trade name used for planning services.</p>
    </div>
    <div class="fcol"><h4>Quick Links</h4><ul><li>Home</li><li>About Us</li><li>Services</li><li>Contact</li></ul></div>
    <div class="fcol"><h4>Contact Us</h4><ul><li><i></i>Location: 214 Birchline Rd</li><li><i></i>+1 (555) 018-2274</li><li><i></i>hello@fernquill.com</li></ul></div>
    <div class="fcol"><h4>Community</h4><ul><li><i></i>Social page</li><li><i></i>Updates</li><li><i></i>Videos</li><li><i></i>Network</li></ul></div>
    <div class="fcol"><h4>Subscribe Newsletter</h4><p>Stay informed with our latest news.</p><div class="sub-input">Enter your email</div><span class="btn">Subscribe</span></div>
  </div>
  <div class="copy">Copyright © 2025 Fernquill Wealth Planners Inc.</div>
</footer>

</body>
</html>
```